Harbor Ridge Seed Collective business cards

Create a single-sided business card for the Harbor Ridge Seed Collective based on the attached logo.
The additional data fields include Name, Title, Email, Phone, and website.
Please use the following as sample data:
Name: Dana Vellor
Title: Co-Founder / Investor
Email: danavellor@mailbrook.example
Phone: 805-555-0147
Website: www.hrseedcollective.example

Target Market(s)

Start ups, entrepreneurs, venture capitalists

Industry/Entity Type

Investment

Contact Information for Business Card

Professional business card. Technology company.

Font styles to use
Serif
Sans Serif

Requirements
Must have
• Include the HRSC logo (attached)
• Name
• Title
• Email
• Phone
• Website
Should not have
• Cute, cartoony

```html
<!DOCTYPE html>
<html lang="en">
<head>
<meta charset="utf-8">
<title>Harbor Ridge Seed Collective – Business Card</title>
<link href="https://fonts.googleapis.com/css2?family=Source+Sans+3:wght@400;600&display=swap" rel="stylesheet">
<style>
  :root {
    --stage: #000000;
    --card-light: #f3f3f3;
    --card-dark: #454547;
    --brand-green: #218a47;
    --brand-green-deep: #1c7a3e;
    --text-white: #ffffff;
    --text-soft: #e6e6e6;
    --bubble-tint: rgba(255, 255, 255, 0.16);
  }
  * { margin: 0; padding: 0; box-sizing: border-box; }
  html, body {
    width: 1200px; height: 900px; overflow: hidden;
    background: var(--stage);
    font-family: "Source Sans 3", "Myriad Pro", Arial, sans-serif;
  }
  .canvas { position: relative; width: 1200px; height: 900px; }

  .card {
    position: absolute; top: 271px; height: 281px;
    border-radius: 14px; overflow: hidden;
  }
  .card-front { left: 137px; width: 457px; background: var(--card-light); }
  .card-back { left: 626px; width: 458px; background: var(--brand-green); }

  /* front: brand area */
  .brand-lockup {
    position: absolute; left: 0; right: 0; top: 0; height: 190px;
    display: flex; align-items: center; justify-content: center; gap: 18px;
  }
  .brand-mark {
    width: 34px; height: 34px; border-radius: 50%;
    background: var(--brand-green);
  }
  .brand-name {
    color: var(--brand-green);
    font-weight: 400; font-size: 27px; line-height: 1.08;
  }

  /* front: contact band */
  .contact-band {
    position: absolute; left: 0; right: 0; top: 190px; bottom: 0;
    background: var(--card-dark); color: var(--text-white);
  }
  .holder { position: absolute; left: 23px; top: 23px; }
  .holder-name { font-weight: 600; font-size: 18.5px; line-height: 1.1; }
  .holder-title { font-size: 13px; color: var(--text-soft); margin-top: 2px; }

  .contact-list {
    position: absolute; right: 22px; top: 14px;
    list-style: none; text-align: right;
    font-size: 12.5px; line-height: 17.5px;
  }
  .contact-list li { display: flex; justify-content: flex-end; align-items: center; gap: 6px; }
  .contact-icon { width: 10px; height: 10px; fill: var(--text-white); flex: none; }

  /* back */
  .bubble-field {
    position: absolute; right: 0; top: 0; width: 280px; height: 281px;
    background: radial-gradient(ellipse at 70% 50%, var(--bubble-tint), rgba(255,255,255,0) 70%);
  }
  .back-name {
    position: absolute; left: 0; right: 0; top: 106px;
    text-align: center; color: var(--text-white);
    font-weight: 400; font-size: 36px; line-height: 1.05;
  }
</style>
</head>
<body>
<main class="canvas">

  <section class="card card-front" aria-label="Business card front">
    <div class="brand-lockup">
      <span class="brand-mark" aria-hidden="true"></span>
      <div class="brand-name">Harbor Ridge<br>Seed Collective</div>
    </div>

    <div class="contact-band">
      <div class="holder">
        <p class="holder-name">Dana Vellor</p>
        <p class="holder-title">Co-Founder / Investor</p>
      </div>
      <ul class="contact-list">
        <li>805-555-0147
          <svg class="contact-icon" viewBox="0 0 10 10" aria-hidden="true">
            <path d="M1 3.2C1 2 2.6 1.3 5 1.3S9 2 9 3.2v.8H7V3c-.6-.3-3.4-.3-4 0v1H1z"/>
            <rect x="2" y="4.5" width="6" height="4" rx="0.6"/>
          </svg>
        </li>
        <li>danavellor@mailbrook.example
          <svg class="contact-icon" viewBox="0 0 10 10" aria-hidden="true">
            <path d="M0.5 2h9v6h-9z M0.5 2L5 5.5 9.5 2" fill="var(--text-white)" stroke="var(--card-dark)" stroke-width="0.8"/>
          </svg>
        </li>
        <li>www.hrseedcollective.example
          <svg class="contact-icon" viewBox="0 0 10 10" aria-hidden="true">
            <circle cx="5" cy="5" r="4.6"/>
            <path d="M3 3.5l2-.8 1 1.2-1.2 1.3.6 1.8-1.4.8-.4-1.8-1.3-.8z" fill="var(--card-dark)"/>
          </svg>
        </li>
      </ul>
    </div>
  </section>

  <section class="card card-back" aria-label="Business card back">
    <div class="bubble-field" role="img" aria-label="Soft scattered translucent circle pattern"></div>
    <div class="back-name">Harbor Ridge<br>Seed Collective</div>
  </section>

</main>
</body>
</html>
```